Charity donation cards

I need a card in an envelope that would be given out to people and they would put their donations along with their details (name and email) and give it back to us (dropped in acrylic boxes at events etc).

The card should be a medium size, bi or tri fold to be able to fit all the information i require.

The Sarwa Fund

The Bright Meadow Centre is dedicated to providing the much needed support to families and children struggling with their differences through a holistic and comprehensive approach that includes detailed evaluations, therapy programs and support services to help unlock the potential in every child.

We are so proud to be able to help empower our society by dedicating our business to the mental, physical and social well being of our younger community and pledging all our net profits to help ensure no child is ever left behind.

Professional services can often be expensive. Our Sarwa Fund helps support families requiring financial aid. We believe every child deserves the opportunity to succeed and no child should be left behind.

How can you help?

Gift the therapies to the children that need it the most. We welcome new sponsors, appreciate your gifts and gratefully accept your contributions as we expand to increase the number of children we can serve.

Name:
Email:
Amount:

We accept cash, checks or credit card payments at The Bright Meadow Centre.

Gift cards should be dropped in the designated acrylic boxes at TBMC or the event.

Please email sarwafund@tbmc-example.ae for more information on the process.
Http://www.tbmc-example.ae

Target Market(s)

These cards will be placed in the reception for our clients to donate.

We will also be working with party planners. Some parents don't want people to get them gifts for their kids birthday party so they want to use this instead.

Industry/Entity Type

Charity

Requirements
Must have
• The same feel as our centre Http://www.tbmc-example.ae
• our website, email and contact number
Nice to have
• Go to our website and feel free to take ideas and content.
• The design should be clean and simple.
• High light the key words in the text with bold and maybe in green to make it pop out.
Should not have
• Do not use the word donate in any print material. The word should be gift.

```html
<!DOCTYPE html>
<html lang="en">
<head>
<meta charset="utf-8">
<title>The Sarwa Fund – Gift Card Set</title>
<link rel="stylesheet" href="https://fonts.googleapis.com/css2?family=Questrial&family=Gochi+Hand&display=swap">
<style>
  :root {
    --backdrop: #d6d6d6;
    --sleeve: #e6e6e7;
    --paper: #ffffff;
    --ink: #666666;
    --ink-soft: #777777;
    --green: #8dc63f;
    --blue: #5bb6d2;
    --orange: #eaa93c;
    --red: #d9582b;
    --leaf: #8cc04a;
  }
  * { box-sizing: border-box; margin: 0; padding: 0; }
  html, body {
    width: 1200px; height: 660px; overflow: hidden;
    background: var(--backdrop);
    font-family: "Questrial", "Century Gothic", sans-serif;
    color: var(--ink);
  }
  .canvas { position: relative; width: 1200px; height: 660px; }

  /* Letter card */
  .letter {
    position: absolute; left: 608px; top: 33px;
    width: 487px; height: 603px;
    background: var(--paper);
    padding: 56px 56px 0 52px;
    font-size: 9.8px; line-height: 11.8px;
  }
  .letter__title { color: var(--green); font-size: 12px; font-weight: 400; margin-bottom: 12px; }
  .letter p { margin-bottom: 11.6px; }
  .letter a { color: var(--green); text-decoration: none; }
  .letter__signature {
    font-family: "Gochi Hand", cursive;
    font-size: 15px; color: #444; margin-top: 6px; padding-left: 4px;
  }
  .letter__artwork {
    position: absolute; left: 78px; top: 408px;
    width: 310px; height: 195px;
    background: linear-gradient(90deg, var(--orange) 0%, var(--blue) 30%, var(--leaf) 55%, var(--red) 75%, var(--orange) 100%);
    opacity: 0.85;
    border-radius: 40% 40% 0 0 / 30% 30% 0 0;
  }

  /* Envelope sleeve */
  .sleeve { position: absolute; left: 45px; top: 32px; width: 566px; height: 300px; }
  .sleeve__shape { position: absolute; inset: 0; }
  .sleeve__content { position: absolute; inset: 0; padding: 0 0 0 44px; }
  .brand {
    position: absolute; left: 44px; top: 88px;
    display: flex; align-items: center; gap: 12px;
  }
  .brand__dot { width: 28px; height: 28px; border-radius: 50%; background: var(--green); }
  .brand__name { font-size: 22px; color: var(--ink); line-height: 1; }
  .sleeve__info {
    position: absolute; left: 44px; top: 190px;
    font-size: 9.8px; line-height: 12px; color: var(--ink-soft);
  }
  .sleeve__info p + p { margin-top: 11px; }
</style>
</head>
<body>
<main class="canvas">

  <article class="letter">
    <h1 class="letter__title">Sarwa (Gift) Fund</h1>
    <p>The Bright Meadow Centre was born and established in the UAE.</p>
    <p>We are so proud to be able to help empower our society by dedicating our business to the mental, physical and social well being of our younger community.</p>
    <p>Professional services can often be expensive. Our Sarwa (Gift) Fund helps support families requiring financial aid.</p>
    <p>We believe every child deserves the opportunity to succeed and no child should be left behind. That is why TBMC is a social business, gifting all of its net profit to the Sarwa fund.</p>
    <p>The sole purpose of the Sarwa fund will be to support families in the Emirates that require financial aid to subsidize the cost of evaluations, therapies and support needed to help children succeed and reach their potential.</p>
    <p>The financial grant services will be accessible to all families &amp; nationalities in the Emirates that meet the criteria.</p>
    <p>We welcome new sponsors, appreciate your gifts and gratefully accept your contributions as we expand to increase the number of children we can serve.</p>
    <p>Please, visit our website <a href="#">www.tbmc-example.ae</a> to learn more about our activities.</p>
    <p>Sincerely,</p>
    <div class="letter__signature">Lina Haddad &amp; Mira Saleh.</div>
    <div class="letter__artwork" role="img" aria-label="Illustration of many raised colourful hands in blue, orange, green and red"></div>
  </article>

  <section class="sleeve">
    <svg class="sleeve__shape" width="566" height="300" viewBox="0 0 566 300" aria-hidden="true">
      <path d="M0 0 H566 V137 A34 34 0 0 0 566 205 V300 H0 Z" fill="var(--sleeve)"/>
    </svg>
    <div class="brand">
      <span class="brand__dot"></span>
      <span class="brand__name">The Bright Meadow Centre</span>
    </div>
    <div class="sleeve__info">
      <p>Please visit our website to learn more about out activities<br>or email for more information on the process</p>
      <p>web: www.tbmc-example.ae<br>email: sarwafund@tbmc-example.ae</p>
    </div>
  </section>

</main>
</body>
</html>
```